Tally Harbor Cover lead generation web-site.

A Multi-purpose lead generation site with unique selling proposition, hero shot, benefits, social proof, and call-to-action. looking for a clean, modern site that is scalable. The site should be search engine optimized.

Reason: Will be reviewing designs submitted and ask for changes if any.

Target Market(s)

Homeowner and automobile owners that also own busineses.

Industry/Entity Type

Insurance

Coding

Coded - Design and coding required

Number of Pages Required

5+ page

Font styles to use
Serif

Requirements
Must have
• Optimization for mobile devices, a clean site similar to (https://plumvergepolicy.com), Easy to use, Interactivity, and easy content management. Quote forms for personal and commercial auto, homeowners, business owners insurance. Pixtrell on pages (analytics)
Nice to have
• Uses of Technology similar to https://brelvanta.com. Integration or ability to push to third-party tools. Auto email responses, Chat integration, social media (join our group, sign up RSS feeds).
Should not have
• Links that closes our site.

```html
<!DOCTYPE html>
<html lang="en">
<head>
<meta charset="utf-8">
<title>Tally Harbor Cover – Insurance Quotes</title>
<link href="https://fonts.googleapis.com/css2?family=Open+Sans:wght@400;600;700&display=swap" rel="stylesheet">
<style>
:root{
  --navy:#1e416b;
  --blue:#0f75b5;
  --blue-light:#2c8fcf;
  --text:#333;
  --muted:#555;
  --line:#c8d3df;
  --grey-band:#e8e8e8;
  --arrow:#9ea3a8;
  --star:#f0a91a;
  --white:#fff;
}
*{box-sizing:border-box;margin:0;padding:0}
html,body{width:701px;height:1200px;overflow:hidden;background:var(--white)}
body{font-family:'Open Sans',sans-serif;color:var(--text);position:relative}
.abs{position:absolute}

/* header */
.site-header{left:0;top:0;width:701px;height:61px;background:var(--white)}
.brand{left:58px;top:16px;display:flex;align-items:center;gap:6px}
.brand-mark{width:24px;height:24px;border-radius:50%;background:var(--navy)}
.brand-name{font-size:15px;font-weight:400;color:var(--navy);line-height:1}
.main-nav{right:78px;top:27px;display:flex;gap:17px;font-size:7.6px;color:#333}
.main-nav .active{color:var(--blue);font-weight:700}

/* hero */
.hero{left:0;top:61px;width:701px;height:262px;
  background:linear-gradient(100deg,#2f4a2c 0%,#4b6a3a 18%,#b9b7b4 38%,#d8d2c6 55%,#7a8d6a 78%,#2f4328 100%)}
.quote-box{left:58px;top:91px;width:178px;height:190px;background:var(--navy);padding:20px 15px 0}
.quote-box h2{font-size:15.5px;font-weight:700;color:var(--white);text-align:center;letter-spacing:.2px}
.quote-box .field{height:19px;background:var(--white);border-radius:2px;margin-top:12px;font-size:7px;color:var(--blue);padding:5px 10px;line-height:1}
.quote-box .field:first-of-type{margin-top:12px}
.quote-box .btn{display:block;margin:10px auto 0;width:93px;height:20px;border-radius:2px;
  background:linear-gradient(#2f9ad8,#1677b8);color:var(--white);font-size:10px;font-weight:600;text-align:center;line-height:20px}

/* welcome */
.welcome-title{left:0;top:343px;width:701px;text-align:center;font-size:12.4px;font-weight:700;color:var(--navy)}
.welcome-text{left:74px;top:370px;width:553px;text-align:center;font-size:6.8px;line-height:12px;color:var(--muted)}
.btn-read{left:317px;top:430px;width:67px;height:19px;border-radius:2px;background:linear-gradient(#2f9ad8,#1677b8);
  color:var(--white);font-size:8px;font-weight:600;text-align:center;line-height:19px}

/* benefits / features */
.col-title{font-size:12px;font-weight:700;color:var(--navy);top:477px}
.col-divider{left:350px;top:482px;width:1px;height:258px;background:var(--line)}
.item{width:260px;height:66px}
.item .diamond{left:0;top:0;width:66px;height:66px}
.item h3{left:61px;top:0;font-size:9px;font-weight:700;color:#222;letter-spacing:.1px}
.item p{left:61px;top:13px;width:180px;font-size:6.3px;line-height:12px;color:var(--muted)}

/* testimonials */
.testi-title{left:0;top:766px;width:701px;text-align:center;font-size:12px;font-weight:700;color:var(--navy)}
.badge{left:333px;top:789px;width:34px;height:34px;border-radius:50%;background:#b8231e}
.stars{left:320px;top:826px;display:flex;gap:3px}
.testi-heading{left:0;top:848px;width:701px;text-align:center;font-size:8.4px;font-weight:700;letter-spacing:2.3px;color:#444}
.testi-text{left:98px;top:871px;width:506px;text-align:center;font-size:6.3px;line-height:12px;color:var(--muted)}
.testi-author{left:0;top:930px;width:701px;text-align:center;font-size:8px;font-weight:700;color:#333}
.arrows{left:327px;top:956px;display:flex;gap:2px}
.arrow{width:23px;height:24px;background:var(--arrow)}

/* footer */
.site-footer{left:0;top:1010px;width:701px;height:101px;background:var(--navy)}
.footer-nav{left:0;top:1034px;width:701px;display:flex;justify-content:center;gap:17px;font-size:7.6px;font-weight:700;color:var(--white)}
.social{left:311px;top:1065px;display:flex;gap:6px}
.social span{width:15px;height:15px;border-radius:2px;background:var(--blue-light)}
.copyright{left:0;top:1093px;width:701px;text-align:center;font-size:7px;font-weight:700;color:var(--white)}
.disclaimer{left:0;top:1111px;width:701px;height:89px;background:var(--grey-band)}
.disclaimer h4{position:absolute;left:0;top:13px;width:701px;text-align:center;font-size:8px;font-weight:700;letter-spacing:2.4px;color:#222}
.disclaimer p{position:absolute;left:78px;top:30px;width:545px;text-align:center;font-size:6.3px;line-height:15px;color:#444}
</style>
</head>
<body>

<header class="site-header abs">
  <div class="brand abs"><span class="brand-mark"></span><span class="brand-name">Tally Harbor Cover</span></div>
  <nav class="main-nav abs">
    <span class="active">HOME</span><span>ABOUT US</span><span>BENEFITS</span><span>FEATURES</span><span>TESTIMONIALS</span><span>CONTACT US</span>
  </nav>
</header>

<section class="hero abs" role="img" aria-label="Photo of a large white family house with lit windows, front stairs and a green garden at dusk"></section>

<form class="quote-box abs">
  <h2>REQUEST A QUOTE</h2>
  <div class="field">Enter Name</div>
  <div class="field">Telephone</div>
  <div class="field">Email</div>
  <span class="btn">Get a Quote</span>
</form>

<h1 class="welcome-title abs">WELCOME TO TALLY HARBOR COVER</h1>
<p class="welcome-text abs">Quis autem vel eum iure reprehenderit qui in ea voluptate velit esse quam nihil molestiae consequatur, vel illum qui dolorem eum fugiat quo voluptas nulla pariatur Sed ut perspiciatis unde omnis iste natus error sit voluptatem accusantium doloremque laudantium, totam rem aperiam, eaque ipsa quae ab illo inventore veritatis et quasi architecto beatae vitae dicta sunt explicabo. Nemo enim ipsam voluptatem quia voluptas sit aspernatur aut odit aut fugit, sed quia consequuntur magni dolores eos qui ratione voluptatem sequi nesciunt.</p>
<span class="btn-read abs">Read More</span>

<h2 class="col-title abs" style="left:78px">OUR BENEFITS</h2>
<h2 class="col-title abs" style="left:383px">OUR FEATURES</h2>
<div class="col-divider abs"></div>

<svg width="0" height="0" style="position:absolute">
  <defs>
    <symbol id="diamond-navy" viewBox="0 0 66 66">
      <path d="M33 1 L65 33 L33 65 L1 33Z" fill="none" stroke="#1e416b" stroke-width="1"/>
      <path d="M33 4 L62 33 L33 62 L4 33Z" fill="#1e416b"/>
    </symbol>
    <symbol id="diamond-blue" viewBox="0 0 66 66">
      <path d="M33 1 L65 33 L33 65 L1 33Z" fill="none" stroke="#0f75b5" stroke-width="1"/>
      <path d="M33 4 L62 33 L33 62 L4 33Z" fill="#0f75b5"/>
    </symbol>
  </defs>
</svg>

<!-- benefits -->
<div class="item abs" style="left:72px;top:509px">
  <svg class="diamond abs" viewBox="0 0 66 66"><use href="#diamond-navy"/>
    <g fill="#fff" transform="translate(33 33)">
      <circle r="7"/><g stroke="#fff" stroke-width="3.2"><path d="M0-10V10M-10 0H10M-7-7L7 7M7-7L-7 7"/></g>
      <circle r="3" fill="#1e416b"/>
    </g></svg>
  <h3 class="abs">FINIBUS BONORUM ET MALORUM</h3>
  <p class="abs">Lorem ipsum dolor sit amet, consectetur adipiscing elit, sed do eiusmod tempor incididunt ut labore et dolore magna aliqua.</p>
</div>
<div class="item abs" style="left:72px;top:584px">
  <svg class="diamond abs" viewBox="0 0 66 66"><use href="#diamond-navy"/>
    <ellipse cx="33" cy="31" rx="11" ry="8" fill="#fff"/><path d="M26 36 L24 42 L31 38Z" fill="#fff"/>
    <g fill="#1e416b"><circle cx="28" cy="31" r="1.6"/><circle cx="33" cy="31" r="1.6"/><circle cx="38" cy="31" r="1.6"/></g></svg>
  <h3 class="abs">FINIBUS BONORUM ET MALORUM</h3>
  <p class="abs">Lorem ipsum dolor sit amet, consectetur adipiscing elit, sed do eiusmod tempor incididunt ut labore et dolore magna aliqua.</p>
</div>
<div class="item abs" style="left:72px;top:660px">
  <svg class="diamond abs" viewBox="0 0 66 66"><use href="#diamond-navy"/>
    <path d="M25 21H37L42 26V45H25Z" fill="#fff"/>
    <g stroke="#1e416b" stroke-width="1.4"><path d="M28 30H39M28 34H39M28 38H39M28 42H39"/></g></svg>
  <h3 class="abs">FINIBUS BONORUM ET MALORUM</h3>
  <p class="abs">Lorem ipsum dolor sit amet, consectetur adipiscing elit, sed do eiusmod tempor incididunt ut labore et dolore magna aliqua.</p>
</div>

<!-- features -->
<div class="item abs" style="left:373px;top:509px">
  <svg class="diamond abs" viewBox="0 0 66 66"><use href="#diamond-blue"/>
    <rect x="26" y="21" width="14" height="24" fill="#fff"/>
    <g fill="#0f75b5"><rect x="28" y="24" width="3" height="3"/><rect x="32" y="24" width="3" height="3"/><rect x="36" y="24" width="2" height="3"/>
    <rect x="28" y="29" width="3" height="3"/><rect x="32" y="29" width="3" height="3"/><rect x="36" y="29" width="2" height="3"/>
    <rect x="28" y="34" width="3" height="3"/><rect x="32" y="34" width="3" height="3"/><rect x="36" y="34" width="2" height="3"/>
    <rect x="31" y="40" width="4" height="5"/></g></svg>
  <h3 class="abs">FINIBUS BONORUM ET MALORUM</h3>
  <p class="abs">Lorem ipsum dolor sit amet, consectetur adipiscing elit, sed do eiusmod tempor incididunt ut labore et dolore magna aliqua.</p>
</div>
<div class="item abs" style="left:373px;top:584px">
  <svg class="diamond abs" viewBox="0 0 66 66"><use href="#diamond-blue"/>
    <path d="M21 33 L33 22 L45 33" fill="none" stroke="#fff" stroke-width="3"/>
    <path d="M25 33 L33 26 L41 33 V43 H36 V37 H30 V43 H25Z" fill="#fff"/></svg>
  <h3 class="abs">FINIBUS BONORUM ET MALORUM</h3>
  <p class="abs">Lorem ipsum dolor sit amet, consectetur adipiscing elit, sed do eiusmod tempor incididunt ut labore et dolore magna aliqua.</p>
</div>
<div class="item abs" style="left:373px;top:660px">
  <svg class="diamond abs" viewBox="0 0 66 66"><use href="#diamond-blue"/>
    <path d="M22 44 V24 H26 V32 L32 28 V32 L38 28 V32 L44 28 V44Z" fill="#fff"/></svg>
  <h3 class="abs">FINIBUS BONORUM ET MALORUM</h3>
  <p class="abs">Lorem ipsum dolor sit amet, consectetur adipiscing elit, sed do eiusmod tempor incididunt ut labore et dolore magna aliqua.</p>
</div>

<!-- testimonials -->
<h2 class="testi-title abs">TESTIMONIALS</h2>
<div class="badge abs" aria-label="Review listing badge"></div>
<div class="stars abs" aria-label="4.5 out of 5 stars">
  <svg width="9" height="9" viewBox="0 0 10 10"><path d="M5 0L6.2 3.6H10L6.9 5.8L8.1 9.5L5 7.2L1.9 9.5L3.1 5.8L0 3.6H3.8Z" fill="var(--star)"/></svg>
  <svg width="9" height="9" viewBox="0 0 10 10"><path d="M5 0L6.2 3.6H10L6.9 5.8L8.1 9.5L5 7.2L1.9 9.5L3.1 5.8L0 3.6H3.8Z" fill="var(--star)"/></svg>
  <svg width="9" height="9" viewBox="0 0 10 10"><path d="M5 0L6.2 3.6H10L6.9 5.8L8.1 9.5L5 7.2L1.9 9.5L3.1 5.8L0 3.6H3.8Z" fill="var(--star)"/></svg>
  <svg width="9" height="9" viewBox="0 0 10 10"><path d="M5 0L6.2 3.6H10L6.9 5.8L8.1 9.5L5 7.2L1.9 9.5L3.1 5.8L0 3.6H3.8Z" fill="var(--star)"/></svg>
  <svg width="9" height="9" viewBox="0 0 10 10"><path d="M5 0L6.2 3.6H10L6.9 5.8L8.1 9.5L5 7.2L1.9 9.5L3.1 5.8L0 3.6H3.8Z" fill="none" stroke="var(--star)" stroke-width=".8"/><path d="M5 0V7.2L1.9 9.5L3.1 5.8L0 3.6H3.8Z" fill="var(--star)"/></svg>
</div>
<h3 class="testi-heading abs">FINIBUS BONORUM ET MALORUM</h3>
<p class="testi-text abs">Sed ut perspiciatis unde omnis iste natus error sit voluptatem accusantium doloremque laudantium, totam rem aperiam, eaque ipsa quae ab illo inventore veritatis et quasi architecto beatae vitae dicta sunt explicabo. Nemo enim ipsam voluptatem quia voluptas sit aspernatur aut odit aut fugit, sed quia consequuntur magni dolores eos qui ratione voluptatem sequi nesciunt. Neque porro quisquam est, qui dolorem ipsum quia dolor sit amet, consectetur, adipisci velit, sed quia non numquam eius modi tempora incidunt ut labore et dolore magnam aliquam quaerat voluptatem.</p>
<p class="testi-author abs">-Mira Okten</p>
<div class="arrows abs">
  <svg class="arrow" viewBox="0 0 23 24"><rect width="23" height="24" fill="var(--arrow)"/><path d="M13 8L9 12L13 16" fill="none" stroke="#fff" stroke-width="1.3"/></svg>
  <svg class="arrow" viewBox="0 0 23 24"><rect width="23" height="24" fill="var(--arrow)"/><path d="M10 8L14 12L10 16" fill="none" stroke="#fff" stroke-width="1.3"/></svg>
</div>

<footer class="site-footer abs"></footer>
<nav class="footer-nav abs"><span>HOME</span><span>ABOUT US</span><span>BENEFITS</span><span>FEATURES</span><span>TESTIMONIALS</span><span>CONTACT US</span></nav>
<div class="social abs" aria-label="Social links"><span></span><span></span><span></span><span></span></div>
<p class="copyright abs">© 2017. www.tallyharborcover.com</p>

<section class="disclaimer abs">
  <h4>DISCLAIMER :</h4>
  <p>Sed ut perspiciatis unde omnis iste natus error sit voluptatem accusantium doloremque laudantium, totam rem aperiam, eaque ipsa quae ab illo inventore veritatis et quasi architecto beatae vitae dicta sunt explicabo. Nemo enim ipsam voluptatem quia voluptas sit aspernatur aut odit aut fugit, sed quia consequuntur magni dolores eos qui ratione voluptatem sequi nesciunt.</p>
</section>

</body>
</html>
```